Business card based on your logo design "Brennock&Co"

Can you please design a business card based on the logo artwork you designed for our business. Double sided as per your submitted image of possible application of logo.

```html
<!DOCTYPE html>
<html lang="en">
<head>
<meta charset="utf-8">
<title>Brennock&amp;Co business card</title>
<link rel="stylesheet" href="https://fonts.googleapis.com/css2?family=Michroma&display=swap">
<style>
  :root {
    --bg: #e8e5e0;
    --charcoal: #333436;
    --paper: #ffffff;
    --paper-shade: #eeeeee;
    --orange: #f7941d;
    --ink: #2b2b2b;
    --ink-soft: #444;
  }
  html, body {
    margin: 0;
    padding: 0;
    width: 1200px;
    height: 1019px;
    overflow: hidden;
    background: var(--bg);
    font-family: "Michroma", sans-serif;
  }
  .canvas {
    position: relative;
    width: 1200px;
    height: 1019px;
  }
  .card {
    position: absolute;
    left: 220px;
    width: 760px;
    height: 434px;
    box-shadow: 0 10px 26px rgba(0,0,0,.22);
    overflow: hidden;
  }
  /* Front: logo side */
  .card-front {
    top: 45px;
    background: var(--charcoal);
  }
  .front-panel {
    position: absolute;
    left: 0;
    top: 0;
    width: 716px;
    height: 276px;
    background: linear-gradient(160deg, var(--paper) 40%, var(--paper-shade));
    display: flex;
    flex-direction: column;
    align-items: center;
    justify-content: center;
  }
  .brand-name {
    font-size: 50px;
    color: var(--ink);
    letter-spacing: 1px;
    text-transform: uppercase;
    margin: 0;
  }
  .brand-tagline {
    margin-top: 14px;
    font-size: 11px;
    color: var(--ink-soft);
    letter-spacing: 2px;
  }
  .holder {
    position: absolute;
    left: 0;
    right: 44px;
    top: 300px;
    text-align: center;
    color: var(--paper);
  }
  .holder-name {
    font-size: 26px;
    letter-spacing: 3px;
    margin: 0 0 10px;
  }
  .holder-role {
    font-size: 19px;
    letter-spacing: 3px;
    margin: 0;
  }
  /* Back: contact side */
  .card-back {
    top: 540px;
    background: linear-gradient(160deg, var(--paper) 50%, var(--paper-shade));
  }
  .back-strip {
    position: absolute;
    left: 0;
    top: 0;
    width: 34px;
    height: 100%;
    background: var(--charcoal);
  }
  .contact-list {
    list-style: none;
    margin: 0;
    padding: 0;
    position: absolute;
    left: 70px;
    top: 44px;
  }
  .contact-item {
    display: flex;
    align-items: center;
    height: 58px;
    font-size: 17px;
    color: var(--ink);
    letter-spacing: 1px;
  }
  .contact-icon {
    width: 36px;
    height: 36px;
    margin-right: 20px;
    flex: none;
  }
</style>
</head>
<body>
<div class="canvas">
  <section class="card card-front" aria-label="Card front">
    <div class="front-panel">
      <h1 class="brand-name">Brennock&amp;Co</h1>
      <div class="brand-tagline">Building and Project Management</div>
    </div>
    <div class="holder">
      <p class="holder-name">LIAM HARLOW</p>
      <p class="holder-role">GENERAL MANAGER</p>
    </div>
  </section>

  <section class="card card-back" aria-label="Card back">
    <div class="back-strip"></div>
    <ul class="contact-list">
      <li class="contact-item">
        <svg class="contact-icon" viewBox="0 0 36 36" aria-hidden="true"><rect width="36" height="36" rx="5" fill="#f7941d"/><path d="M12 9c1.5 0 3 3.5 3 4.5S13 15 13.5 16.5s4.5 6 6 6.5 2-1.8 3-1.8 4.5 1.5 4.5 3-2 3-4 3C16 27 9 20 9 13c0-2 1.5-4 3-4z" fill="#fff"/></svg>
        021 555 0142
      </li>
      <li class="contact-item">
        <svg class="contact-icon" viewBox="0 0 36 36" aria-hidden="true"><rect width="36" height="36" rx="5" fill="#f7941d"/><rect x="12" y="7" width="12" height="22" rx="2" fill="#fff"/><rect x="14" y="10" width="8" height="13" fill="#f7941d"/><circle cx="18" cy="26" r="1.3" fill="#f7941d"/></svg>
        021 555 0187
      </li>
      <li class="contact-item">
        <svg class="contact-icon" viewBox="0 0 36 36" aria-hidden="true"><rect width="36" height="36" rx="5" fill="#f7941d"/><rect x="12" y="8" width="12" height="8" fill="#fff"/><rect x="8" y="15" width="20" height="10" rx="2" fill="#fff"/><rect x="12" y="22" width="12" height="7" fill="#fff" stroke="#f7941d" stroke-width="1.5"/></svg>
        021 555 0193
      </li>
      <li class="contact-item">
        <svg class="contact-icon" viewBox="0 0 36 36" aria-hidden="true"><rect width="36" height="36" rx="5" fill="#f7941d"/><rect x="8" y="11" width="20" height="14" fill="#fff"/><path d="M8 11l10 8 10-8" fill="none" stroke="#f7941d" stroke-width="1.8"/></svg>
        liam@brennockco.com
      </li>
      <li class="contact-item">
        <svg class="contact-icon" viewBox="0 0 36 36" aria-hidden="true"><rect width="36" height="36" rx="5" fill="#f7941d"/><g fill="none" stroke="#fff" stroke-width="1.8"><circle cx="18" cy="18" r="10"/><ellipse cx="18" cy="18" rx="4.5" ry="10"/><path d="M8 18h20M10 12.5h16M10 23.5h16"/></g></svg>
        www.brennockco.com
      </li>
      <li class="contact-item">
        <svg class="contact-icon" viewBox="0 0 36 36" aria-hidden="true"><rect width="36" height="36" rx="5" fill="#f7941d"/><path d="M18 29s-8-8.5-8-14a8 8 0 0 1 16 0c0 5.5-8 14-8 14z" fill="#fff"/><circle cx="18" cy="15" r="3" fill="#f7941d"/></svg>
        27 Harbour Row, 4th floor, Dunmore
      </li>
    </ul>
  </section>
</div>
</body>
</html>
```